Building Certification Company needs a professional letterhead and report template

We are a modern company within an ageing industry. Our industry is responsible for life safety aspects of the built environment, we ensure buildings are safe and fit for occupation.

We use letterhead and reports everyday, we need a smart and professional letterhead that reflects the serious nature of the work we do. We also require a report template of the same ilk.

Target Market(s)

Our target market will consist mainly of professional architects, developers and construction companies.

Requirements
Must have
• The letterhead must have:-
Our logo
Our company details, including address, website, email, phone

Address - Suite 208 / 43 Greyfern Avenue Tallowmere NSW 2100

Website - www.harbourlinestructureaudits.com.au

Email - info@hlsa.com.au

Phone - 02 8364 5208

The report template must have:-
A title page, which is to incorporate our logo or an aspect of our logo, get creative people.

```html
<!DOCTYPE html>
<html lang="en">
<head>
<meta charset="utf-8">
<title>Harbourline Structure Audits — Letterhead</title>
<link href="https://fonts.googleapis.com/css2?family=Tinos:ital@0;1&family=Questrial&family=Mrs+Saint+Delafield&display=swap" rel="stylesheet">
<style>
  :root {
    --backdrop: #e6e6e6;
    --paper: #ffffff;
    --ink: #1c1c1c;
    --brand-blue: #3a4fa0;
    --footer-ink: #3b3b3b;
  }
  * { box-sizing: border-box; margin: 0; padding: 0; }
  html, body { width: 1200px; height: 900px; overflow: hidden; }
  body { background: var(--backdrop); display: flex; align-items: center; justify-content: center; }
  .letterhead {
    position: relative;
    width: 608px; height: 860px;
    background: var(--paper);
    box-shadow: 0 2px 10px rgba(0,0,0,.15);
    padding: 56px 58px 0 58px;
    color: var(--ink);
    font-family: "Tinos", "Times New Roman", serif;
  }
  .brand { display: flex; align-items: center; gap: 10px; }
  .brand-square { width: 22px; height: 22px; background: var(--brand-blue); }
  .brand-name {
    font-family: "Questrial", sans-serif;
    color: var(--brand-blue);
    font-size: 17px; letter-spacing: .12em; text-transform: uppercase;
  }
  .letter-body { margin-top: 44px; font-size: 12.2px; line-height: 1.32; text-align: justify; }
  .letter-body p { margin-bottom: 14px; }
  .salutation { margin-bottom: 12px; }
  .closing { margin-top: 44px; font-size: 12.5px; line-height: 1.35; }
  .signature { font-family: "Mrs Saint Delafield", cursive; font-size: 38px; line-height: 1; margin: 6px 0 2px; }
  .contact {
    position: absolute; right: 48px; bottom: 40px;
    font-family: "Questrial", sans-serif; font-size: 10px; color: var(--footer-ink);
    display: flex; flex-direction: column; align-items: flex-end; gap: 6px;
  }
  .contact-row { display: flex; gap: 18px; }
  .contact-item { display: flex; align-items: center; gap: 5px; }
  .contact-item svg { width: 9px; height: 9px; fill: var(--brand-blue); }
</style>
</head>
<body>
  <main class="letterhead">
    <header class="brand">
      <span class="brand-square"></span>
      <span class="brand-name">Harbourline Structure Audits</span>
    </header>

    <section class="letter-body">
      <p class="salutation">Gentlemen,</p>
      <p>Enclosed I have the honor to send you an article which I should be pleased if you would accept for the “Civic Quarterly”. I am <em>desperately</em> pushed for money; and in the event of Mr. Callahan’s liking the “Landscape-Garden”, I would take it as an especial favor if you would mail me the amount due for it, so as to reach me here by the 21st, on which day I shall need it. Can you possibly oblige me in this? If you accept the paper I presume you will allow me your usual sum, whatever that is for similar contributions—but I set no price—leaving all to your own liberality. The piece will make 8 of your pages and rather more.</p>
      <p>Will you be kind enough to put the best possible interpretation upon my behavior while in N-York? You must have conceived a <em>queer</em> idea of me—but the simple truth is that Whitfield would insist upon <em>the juleps</em>, and I knew not what I was either doing or saying. The Review of Rowley which I offered you was deficient in a ½ page of commencement, which I had written to supersede the old beginning, and which gave the article the character of a general and retrospective review. No wonder you did not take it—I would have been very much mortified if you had. I hope to see you at some future time, under better auspices.</p>
    </section>

    <section class="closing">
      <p>In the meantime I remain</p>
      <p>Yours very truly,</p>
      <p class="signature">E. H. Marsh</p>
      <p>Edwin Hale Marsh</p>
    </section>

    <footer class="contact">
      <div class="contact-item">Suite 208 / 43 Greyfern Avenue Tallowmere NSW 2100</div>
      <div class="contact-row">
        <span class="contact-item"><svg viewBox="0 0 10 10"><path d="M2 0l2 2-1 1.5c.8 1.6 1.9 2.7 3.5 3.5L8 6l2 2-1.5 2C4 9.5.5 6 0 1.5z"/></svg>02 8364 5208</span>
        <span class="contact-item"><svg viewBox="0 0 10 10"><rect x="0" y="3" width="10" height="7"/><rect x="2" y="0" width="6" height="3"/></svg>02 8364 5208</span>
        <span class="contact-item"><svg viewBox="0 0 10 10"><path d="M0 2h10v6H0z M0 2l5 3.5L10 2" /></svg>info@hlsa.com.au</span>
      </div>
      <div class="contact-item"><svg viewBox="0 0 10 10"><circle cx="5" cy="5" r="5"/></svg>www.harbourlinestructureaudits.com.au</div>
    </footer>
  </main>
</body>
</html>
```